Trade Show Booth Sign Design for Retracting Banner

I need a trade show booth sign designed. It will be for a retractable banner that is double sided with 34 by 81 inch.

I want to incorporate my logo (see attached, have it in other file formats as well) and graphics from my website (https://www.dolbrookteachingadvisory.com/) with parts or all of the following text.

· Educational Content Creation
o Supplemental Textbook Content Development
o E-learning Content Development
· Curriculum Development
o KVTR/Bright Ladder
o Three Dimensional Learning
· Assessment
o Formative Assessments
o Elementary School, Middle School, High School, College, and Business
· Professional Development
o Training
o Facilitation

Target Market(s)

Education

Industry/Entity Type

Education

Font styles to use
Sans Serif

Colors

Designer to choose colors to be used in the design.

Requirements
Must have
• Eye catching and easy to read design
Nice to have
• Would like to see incorporation of my logo and some of the elements of my website images
Should not have
• N/A

```html
<!DOCTYPE html>
<html lang="en">
<head>
<meta charset="utf-8">
<title>Dolbrook Teaching Advisory – Booth Banner</title>
<link rel="stylesheet" href="https://fonts.googleapis.com/css2?family=Anton&family=Oswald:wght@600&family=Arimo:wght@700&family=Tinos&display=swap">
<style>
  :root {
    --navy: #1d2a5c;
    --panel-blue: #4186c7;
    --band-blue: #3f84c6;
    --white: #ffffff;
    --page: #ffffff;
  }
  * { margin: 0; padding: 0; box-sizing: border-box; }
  html, body { width: 1200px; height: 2848px; overflow: hidden; background: var(--page); }
  .banner { position: relative; width: 1200px; height: 2848px; background: var(--page); overflow: hidden; }

  .brand-band { position: absolute; left: 0; top: 80px; width: 1200px; height: 334px; background: var(--navy); }
  .brand-mark {
    position: absolute; left: 36px; top: 30px; width: 420px; height: 420px;
    border-radius: 50%; background: var(--white); border: 5px solid var(--navy);
  }
  .brand-name {
    position: absolute; left: 470px; top: 118px; width: 700px;
    color: var(--white); text-align: center; white-space: nowrap;
  }
  .brand-name .primary {
    display: block; font-family: "Anton", sans-serif; font-size: 150px;
    line-height: 180px; letter-spacing: 6px;
  }
  .brand-name .secondary {
    display: block; font-family: "Tinos", serif; font-size: 66px; line-height: 80px;
  }

  .idea-art {
    position: absolute; left: 0; top: 414px; width: 1200px; height: 366px;
    background: linear-gradient(90deg, #fbe3de 0%, #e3e6f6 25%, #fdf3d2 50%, #fde9da 75%, #e0f0fb 100%);
  }

  .tagline { position: absolute; left: 0; top: 807px; width: 1120px; height: 137px; }
  .tagline svg { position: absolute; inset: 0; }
  .tagline-text {
    position: absolute; left: 100px; top: 0; height: 137px; line-height: 137px; white-space: nowrap;
    color: var(--white); font-family: "Oswald", sans-serif; font-weight: 600;
    font-size: 88px; letter-spacing: 9px;
  }

  .services { position: absolute; left: 0; top: 1035px; width: 1200px; height: 1653px; background: var(--panel-blue); }

  .feature-art {
    position: absolute; width: 360px; height: 360px; border-radius: 50%;
    background: radial-gradient(circle, #2c3a70 0%, var(--navy) 70%);
    border: 8px solid var(--white); box-shadow: 0 0 0 3px var(--navy);
  }
  .feature-art.presentation { left: 808px; top: 1008px; }
  .feature-art.science { left: 808px; top: 1863px; }

  .section-title {
    position: absolute; left: 72px; color: var(--navy); white-space: nowrap;
    font-family: "Anton", sans-serif; font-weight: 400; font-size: 82px; line-height: 86px;
    text-transform: uppercase; letter-spacing: 6px;
  }
  .section-rule { position: absolute; left: 72px; height: 7px; background: var(--white); }

  .item {
    position: absolute; left: 76px; color: var(--white); white-space: nowrap;
    font-family: "Arimo", sans-serif; font-weight: 700; font-size: 43px; line-height: 54px;
    padding-left: 106px;
  }
  .item svg { position: absolute; left: 0; top: 0; width: 70px; height: 54px; }

  .site-footer {
    position: absolute; left: 0; top: 2687px; width: 1200px; height: 161px; background: var(--navy);
    color: var(--white); font-family: "Arimo", sans-serif; font-weight: 700; font-size: 60px;
    line-height: 161px; text-align: center; white-space: nowrap;
  }
</style>
</head>
<body>
<div class="banner">

  <header class="brand-band"></header>
  <div class="brand-mark"></div>
  <div class="brand-name">
    <span class="primary">DOLBROOK</span>
    <span class="secondary">Teaching Advisory</span>
  </div>

  <div class="idea-art" role="img" aria-label="Row of hanging light bulbs made of crumpled colored paper, the center yellow one glowing"></div>

  <div class="tagline">
    <svg width="1120" height="137" viewBox="0 0 1120 137"><polygon points="0,0 1120,0 1035,137 0,137" fill="var(--band-blue)"/></svg>
    <div class="tagline-text">LEARN. GROW. KNOW.</div>
  </div>

  <main class="services"></main>

  <div class="feature-art presentation" role="img" aria-label="Illustration of a presenter showing charts on a projected screen to an audience"></div>
  <div class="feature-art science" role="img" aria-label="Illustration of a flask surrounded by science and education icons"></div>

  <h2 class="section-title" style="top:1100px;">Educational<br>Content Creation</h2>
  <div class="section-rule" style="top:1290px; width:792px;"></div>
  <p class="item" style="top:1342px;"><svg viewBox="0 0 70 54"><polyline points="6,28 26,46 64,6" fill="none" stroke="#fff" stroke-width="11"/></svg>Supplemental Textbook Content<br>Development</p>
  <p class="item" style="top:1503px;"><svg viewBox="0 0 70 54"><polyline points="6,28 26,46 64,6" fill="none" stroke="#fff" stroke-width="11"/></svg>E-learning Content Development</p>

  <h2 class="section-title" style="top:1614px;">Curriculum Development</h2>
  <div class="section-rule" style="top:1717px; width:991px;"></div>
  <p class="item" style="top:1760px;"><svg viewBox="0 0 70 54"><polyline points="6,28 26,46 64,6" fill="none" stroke="#fff" stroke-width="11"/></svg>KVTR/Bright Ladder</p>
  <p class="item" style="top:1870px;"><svg viewBox="0 0 70 54"><polyline points="6,28 26,46 64,6" fill="none" stroke="#fff" stroke-width="11"/></svg>Three Dimensional Learning</p>

  <h2 class="section-title" style="top:1994px;">Assessment</h2>
  <div class="section-rule" style="top:2092px; width:744px;"></div>
  <p class="item" style="top:2140px;"><svg viewBox="0 0 70 54"><polyline points="6,28 26,46 64,6" fill="none" stroke="#fff" stroke-width="11"/></svg>Formative Assessments</p>
  <p class="item" style="top:2248px;"><svg viewBox="0 0 70 54"><polyline points="6,28 26,46 64,6" fill="none" stroke="#fff" stroke-width="11"/></svg>Elementary School, Middle School,<br>High School, College, and Business</p>

  <h2 class="section-title" style="top:2430px;">Professional Development</h2>
  <div class="section-rule" style="top:2529px; width:1024px;"></div>
  <p class="item" style="top:2586px;"><svg viewBox="0 0 70 54"><polyline points="6,28 26,46 64,6" fill="none" stroke="#fff" stroke-width="11"/></svg>Training</p>
  <p class="item" style="top:2586px; left:642px;"><svg viewBox="0 0 70 54"><polyline points="6,28 26,46 64,6" fill="none" stroke="#fff" stroke-width="11"/></svg>Facilitation</p>

  <footer class="site-footer">www.DolbrookTeachingAdvisory.com</footer>

</div>
</body>
</html>
```